Yoga Training Cerificate

Design a certificate of graduation from a Vinyasa Yoga Teacher Training Program.

The attached document is an example of the certificate I received as a graduate from a teacher training program. You can use it as a template.

Stylistically, what you design can be: visually enticing, professional, clean, and modern.

Please develop the "Tidal Lotus" logo and embed it within the certificate.

Please add a circular watermark behind the body of the certificate similar to the one found in the attachment; leave out the words Asana Guild because I am not associated with that organization.

The name of my school is "Tidal Lotus." And it was established in 2017, which you can include.

The certificate affirms that "' 'such-and-such' has successfully completed the Tidal Lotus modern vinyasa yoga training, completing two hundred hours of instruction in practice and theory. Within the power of our institution as a certifying agent we declare Such-and-such, now, a teacher competent to share the gift of yoga with the masses in a safe and effective."

My name -Dennis Halvorsen- should be at bottom with a faux-signature; position title: Tidal Lotus founder.

If you decide to include text on the fringe, like the example, it might include bars of text describing the maxims of the Tidal Lotus school reading:

This is Tidal Lotus
Breath is primary
Evolve the physical culture
Bring your unique expression to the practice
Take Breaks
Freestyle
Close your eyes
Feel deeper into your body
This is active meditation
This is moving meditation
This is modern meditation

And find a way to integrate Emojis like: Fire, Water, Prayer Hands, etc. as you see fit.

Generally, make the certificate look: official, clear and clean. You can base it from the example given. And try and create a graphic design that is more visually capturing then the example.

```html
<!DOCTYPE html>
<html lang="en">
<head>
<meta charset="utf-8">
<title>Tidal Lotus Certificate of Completion</title>
<link rel="stylesheet" href="https://fonts.googleapis.com/css2?family=Pinyon+Script&family=Raleway:wght@400;600&family=Crimson+Text:ital@1&family=Cinzel:wght@500&display=swap">
<style>
  :root {
    --backdrop: #d6ecf7;
    --paper: #ffffff;
    --ink-purple: #452873;
    --ink-text: #2b1c5a;
    --frame-blue: #7b8cc6;
    --frame-dark: #3d2a6e;
    --seal-tint: #dae7ee;
  }
  * { margin: 0; padding: 0; box-sizing: border-box; }
  html, body { width: 1200px; height: 1200px; overflow: hidden; background: var(--backdrop); }
  .canvas { position: relative; width: 1200px; height: 1200px; }
  .certificate { position: absolute; left: 231px; top: 24px; width: 735px; height: 1152px; background: var(--paper); }
  .frame-art { position: absolute; left: 0; top: 0; width: 1200px; height: 1200px; }
  .abs { position: absolute; }

  .title-script {
    left: 400px; top: 78px; width: 400px; text-align: right;
    font-family: "Pinyon Script", cursive; font-size: 112px; line-height: 1; color: var(--ink-purple);
  }
  .title-sub {
    left: 500px; top: 212px; width: 282px; text-align: right;
    font-family: "Raleway", sans-serif; font-variant: small-caps; font-size: 32px; letter-spacing: 1px;
    color: var(--ink-purple); line-height: 1;
  }
  .affirm-text {
    left: 416px; top: 282px; width: 365px; height: 35px; line-height: 35px; text-align: center;
    font-family: "Raleway", sans-serif; font-weight: 600; font-size: 20px; color: #fff;
  }
  .body-copy {
    left: 290px; width: 618px; text-align: center;
    font-family: "Crimson Text", serif; font-style: italic; font-size: 21px; line-height: 26px; color: var(--ink-text);
  }
  .completion { top: 424px; padding: 0 28px; }
  .declaration { top: 541px; }
  .maxims {
    left: 300px; top: 868px; width: 250px; list-style: none;
    font-family: "Raleway", sans-serif; font-size: 15px; line-height: 19.3px; color: var(--ink-text);
  }
  .signer-name {
    left: 640px; top: 1013px; width: 250px; text-align: center;
    font-family: "Cinzel", serif; font-size: 18px; color: var(--ink-purple);
  }
  .signer-role {
    left: 640px; top: 1036px; width: 250px; text-align: center;
    font-family: "Crimson Text", serif; font-style: italic; font-size: 16px; color: var(--ink-text);
  }
</style>
</head>
<body>
<div class="canvas">
  <div class="certificate"></div>

  <svg class="frame-art" viewBox="0 0 1200 1200" aria-hidden="true">
    <!-- seal -->
    <circle cx="598" cy="678" r="166" fill="none" stroke="var(--seal-tint)" stroke-width="10"/>
    <!-- borders -->
    <rect x="248.5" y="42.5" width="701" height="1115" fill="none" stroke="var(--frame-dark)" stroke-width="2"/>
    <rect x="256" y="50" width="686" height="1100" fill="none" stroke="var(--frame-blue)" stroke-width="8"/>
    <!-- corner dots -->
    <g fill="var(--frame-dark)">
      <circle cx="277" cy="74" r="6"/><circle cx="920" cy="74" r="6"/>
      <circle cx="277" cy="1125" r="6"/><circle cx="920" cy="1125" r="6"/>
    </g>
    <!-- tapering corner rules -->
    <g fill="var(--frame-blue)">
      <polygon points="289,71 289,77 456,74"/>
      <polygon points="908,71 908,77 744,74"/>
      <polygon points="289,1122 289,1128 456,1125"/>
      <polygon points="908,1122 908,1128 744,1125"/>
      <polygon points="274,86 280,86 277,252"/>
      <polygon points="917,86 923,86 920,252"/>
      <polygon points="274,1113 280,1113 277,948"/>
      <polygon points="917,1113 923,1113 920,948"/>
    </g>
    <!-- banner -->
    <polygon points="416,282 781,282 774,299.5 781,317 416,317 423,299.5" fill="var(--ink-purple)"/>
    <!-- name & signature lines -->
    <polygon points="336,414 599,411.5 862,414 599,416.5" fill="#111"/>
    <polygon points="648,1006 765,1004.5 882,1006 765,1007.5" fill="#111"/>
  </svg>

  <div class="abs title-script">Certicate</div>
  <div class="abs title-sub">of Completion</div>
  <div class="abs affirm-text">THE CERTIFICATE AFFIRMS THAT</div>

  <p class="abs body-copy completion">has successfully completed the Tidal Lotus modern vinyasa yoga training, completing two hundred hours of instruction in practice and theory.</p>
  <p class="abs body-copy declaration">Within the power of our institution as a certifying agent we declare the person whose name appears above now, a teacher competent to share the gift of yoga with the masses in a safe and effective.</p>

  <ul class="abs maxims">
    <li>This is Tidal Lotus</li>
    <li>Breath is primary</li>
    <li>Evolve the physical culture</li>
    <li>Bring your unique expression to the practice</li>
    <li>Take Breaks</li>
    <li>Freestyle</li>
    <li>Close your eyes</li>
    <li>Feel deeper into your body</li>
    <li>This is active meditation</li>
    <li>This is moving meditation</li>
    <li>This is modern meditation</li>
  </ul>

  <div class="abs signer-name">Dennis Halvorsen</div>
  <div class="abs signer-role">Tidal Lotus founder.</div>
</div>
</body>
</html>
```